1/2 Page B&W Ad for Conference Program

Hi:

We are an industrial and environmental engineering firm in Seattle. We we design facilities and the internal process technologies for advanced renewable energy projects such as biofuels, waste to energy and other biomass to heat, power, steam, fuel or chemical projects.

We are attending www.fernvaleforum.example this month in Toronto. Our package allows to a 1/2 page ad in the conference book.

The specs for the half page BLACK & WHITE ad are: max width: 7.5 inches, max height: 3.5 inches (no bleeds). Any common high resolution format may be provided (EPS, PDF, etc.)

----

K7 Kelton Associates
www.k7keltonassociates.example
+1 (206) 555-0187
Seattle, WA USA

I wish to convey that we are an "industrial engineering firm specializing in advanced renewable energy projects worldwide".

The services we wish to profile are:

* FEED Front End Engineering Design
* Process Engineering, Design & Scale-Up
* Technical Feasibility & Investor Due Diligence Studies
* Project Management

Registered Professional Engineers in the U.S. & Canada. (Maybe in smaller text).

Our logo is attached. I have included a B&W logo but would prefer a cleaner look. Otherwise, feel free to use stock images of industrial scale (oil refinery, power plant, chemical plant, etc) blended with renewable imaging (biodiesel, etc.). We try to stay away from "green washing" such as two hands holding a plant, children playing in a grass field, etc.

Our image is that of industrial professionals working the advanced renewable energy industry.

The ad should show our logo + the contact address above.

We also need a new website but that project is next...

I need to submit the artwork to the conference by end of day Friday, May 8.

Feel free to ask questions! Thanks!!

Todd Marwencki

Target Market(s)

Project developers and investors planning to invest 30M+ $ in designing and building an advanced renewable energy (biodiesel,etc. ) project. Also, private equity firms needing an engineering firm to help them evaluate projects to fund. Technical feasibility studies.

Industry/Entity Type

Industrial

Font styles to use
Sans Serif

Requirements
Nice to have
• Scandinavian style design.
Should not have
• Cheesy "green energy" ads. The industry today is large scale, industrial and serious about profitability - but also embracing new technologies and moving energy in a cleaner direction.
• Cannot use the Image of Halvorn that is uploaded. But this is our project and an example of an industrial scale biodiesel plant.

```html
<!DOCTYPE html>
<html lang="en">
<head>
<meta charset="utf-8">
<title>K7 Kelton Associates – Half Page Ad</title>
<link rel="stylesheet" href="https://fonts.googleapis.com/css2?family=Open+Sans:ital,wght@0,400;0,700;0,800;1,400;1,700&display=swap">
<style>
  :root {
    --page-bg: #e6e3d8;
    --ad-black: #000000;
    --headline: #ffffff;
    --service-grey: #8c8c8c;
    --band-grey: #b5b5b5;
    --band-text: #111111;
    --photo-light: #e4e4e4;
    --photo-mid: #a9a9a9;
    --photo-dark: #5c5c5c;
  }
  * { margin: 0; padding: 0; box-sizing: border-box; }
  html, body {
    width: 1200px; height: 1031px; overflow: hidden;
    background: var(--page-bg);
    font-family: "Open Sans", Arial, sans-serif;
  }
  .ad {
    position: absolute; left: 50px; top: 259px;
    width: 1100px; height: 513px;
    background: var(--ad-black);
    overflow: hidden;
  }
  .ad__photo { position: absolute; inset: 0; width: 1100px; height: 513px; }
  .ad__headline {
    position: absolute; left: 33px; top: 26px; width: 480px;
    color: var(--headline);
    font-weight: 800; font-size: 23px; line-height: 35px;
    letter-spacing: 2.6px; text-transform: uppercase;
    text-align: justify; text-align-last: left;
  }
  .ad__headline span { display: block; text-align: justify; text-align-last: justify; }
  .ad__headline span:last-child { text-align-last: left; }
  .services {
    position: absolute; left: 33px; top: 186px;
    list-style: none;
    color: var(--service-grey);
    font-size: 16.5px; line-height: 24.5px;
  }
  .services li::before { content: "• "; }
  .credentials {
    position: absolute; left: 33px; top: 300px;
    color: var(--headline);
    font-size: 15.5px; font-style: italic; font-weight: 400;
  }
  .credentials b { font-weight: 700; }
  .brand {
    position: absolute; left: 33px; top: 383px;
    display: flex; align-items: center; gap: 14px;
    color: var(--headline);
  }
  .brand__dot { width: 44px; height: 44px; border-radius: 50%; background: var(--headline); }
  .brand__name { font-weight: 700; font-size: 31px; letter-spacing: 0.5px; }
  .contact-band {
    position: absolute; left: 0; bottom: 0; width: 740px; height: 37px;
    background: var(--band-grey);
    color: var(--band-text);
    font-size: 17px; line-height: 37px; padding-left: 20px;
    word-spacing: 2px;
  }
</style>
</head>
<body>
  <section class="ad" aria-label="K7 Kelton Associates half page advertisement">
    <div class="contact-band">+1 (206) 555-0187&nbsp; Seattle, WA USA&nbsp; www.k7keltonassociates.example</div>

    <svg class="ad__photo" viewBox="0 0 1100 513" aria-hidden="false">
      <defs>
        <linearGradient id="plantTones" x1="0" y1="0" x2="0" y2="1">
          <stop offset="0" stop-color="var(--photo-mid)"/>
          <stop offset="0.3" stop-color="var(--photo-dark)"/>
          <stop offset="0.55" stop-color="var(--photo-light)"/>
          <stop offset="0.85" stop-color="var(--photo-mid)"/>
          <stop offset="1" stop-color="var(--photo-dark)"/>
        </linearGradient>
      </defs>
      <path role="img" aria-label="Black and white photo of an industrial biofuel plant with large white storage tanks and piping"
            d="M738 0 C620 70 570 220 595 330 C615 420 660 480 705 513 L1100 513 L1100 0 Z"
            fill="url(#plantTones)"/>
    </svg>

    <h1 class="ad__headline">
      <span>Industrial engineering firm</span>
      <span>specializing in advanced</span>
      <span>renewable energy projects</span>
      <span>worldwide</span>
    </h1>

    <ul class="services">
      <li>FEED Front End Engineering Design</li>
      <li>Process Engineering, Design &amp; Scale-Up</li>
      <li>Technical Feasibility &amp; Investor Due Diligence Studies</li>
      <li>Project Management</li>
    </ul>

    <p class="credentials"><b>Registered Professional Engineers</b> in the <b>U.S.</b> &amp; <b>Canada</b></p>

    <div class="brand">
      <span class="brand__dot"></span>
      <span class="brand__name">K7 Kelton Associates</span>
    </div>
  </section>
</body>
</html>
```